The Wellness Barn Business Card

Info for the front..... (in whichever order and layout looks best)
Carla Penhallow
Physiotherapist
4/37 Upper Creekbank Rd
Tallowbrook
QLD 4712
0462305178
carlapenhallow57@mailbox.example
www.thewellnessbarn.example.au
on the back I would like to be able to write appointments so probably just that heading with lines.
I like a sort of rustic style but mostly professional, colours in naturals, beige, brown, green etc. I dont mind if the logo colour is changed slightly to suit.

```html
<!DOCTYPE html>
<html lang="en">
<head>
<meta charset="utf-8">
<title>The Wellness Barn Business Card</title>
<link rel="stylesheet" href="https://fonts.googleapis.com/css2?family=Montserrat:wght@500;600;700&display=swap">
<style>
  :root {
    --page: #dfdfdf;
    --green: #33461f;
    --grey-text: #5f5f62;
    --rule: #8d8d8d;
    --paper: #ffffff;
    --peach-light: #fbc699;
    --peach: #f7b27c;
    --peach-deep: #f29b5c;
  }
  * { margin: 0; padding: 0; box-sizing: border-box; }
  html, body {
    width: 1200px; height: 1200px; overflow: hidden;
    background: var(--page);
    font-family: "Montserrat", Arial, sans-serif;
  }
  .card {
    position: absolute; left: 180px; width: 867px; height: 498px;
    box-shadow: 0 10px 22px rgba(0,0,0,0.22);
    overflow: hidden;
  }
  /* Appointment side */
  .card--appointments { top: 85px; }
  .card__texture {
    position: absolute; inset: 0;
    background:
      radial-gradient(ellipse at 85% 10%, var(--peach-deep) 0%, transparent 45%),
      radial-gradient(ellipse at 10% 90%, var(--peach-deep) 0%, transparent 40%),
      radial-gradient(ellipse at 50% 50%, var(--peach-light) 0%, var(--peach) 80%);
  }
  .brand-name {
    position: absolute; color: var(--green); font-weight: 700;
    line-height: 1.02; letter-spacing: 0.5px;
  }
  .card--appointments .brand-name {
    left: 0; right: 0; top: 120px; text-align: center; font-size: 54px;
  }
  .write-line {
    position: absolute; left: 156px; width: 553px; height: 1px;
    background: var(--green); opacity: 0.8;
  }
  .write-line--first { top: 365px; }
  .write-line--second { top: 423px; }

  /* Contact side */
  .card--contact { top: 626px; background: var(--paper); }
  .card--contact .brand-name {
    right: 34px; top: 70px; text-align: right; font-size: 32px;
  }
  .accent-bar {
    position: absolute; left: 0; top: 234px; width: 19px; height: 56px;
    background: var(--green); border-radius: 0 5px 5px 0;
  }
  .person-name {
    position: absolute; left: 36px; top: 230px;
    font-size: 36px; font-weight: 500; color: var(--green); letter-spacing: 0.6px;
  }
  .person-role {
    position: absolute; left: 36px; top: 270px;
    font-size: 20px; font-weight: 500; color: var(--grey-text); letter-spacing: 0.6px;
  }
  .divider {
    position: absolute; left: 36px; width: 793px; top: 297px; height: 1px;
    background: var(--rule);
  }
  .contact-list {
    position: absolute; left: 36px; top: 316px; list-style: none;
  }
  .contact-list li {
    display: flex; align-items: center; height: 36px;
    font-size: 19px; font-weight: 600; color: var(--grey-text); letter-spacing: 1.4px;
  }
  .contact-list svg { width: 24px; height: 24px; margin-right: 11px; flex: none; }
  .address {
    position: absolute; right: 38px; top: 316px; text-align: right;
    font-size: 19px; font-weight: 600; color: var(--grey-text); letter-spacing: 1.4px;
    font-style: normal;
  }
  .address span { display: block; height: 36px; line-height: 36px; }
</style>
</head>
<body>

<section class="card card--appointments">
  <div class="card__texture" role="img" aria-label="Warm peach plaster texture background"></div>
  <div class="brand-name">The Wellness<br>Barn</div>
  <div class="write-line write-line--first"></div>
  <div class="write-line write-line--second"></div>
</section>

<section class="card card--contact">
  <div class="brand-name">The Wellness<br>Barn</div>
  <div class="accent-bar"></div>
  <div class="person-name">Carla Penhallow</div>
  <div class="person-role">Physiotherapist</div>
  <div class="divider"></div>

  <ul class="contact-list">
    <li>
      <svg viewBox="0 0 24 24" aria-hidden="true"><path fill="#33461f" d="M6.6 3.5 9.3 6.2c.5.5.5 1.2.1 1.7L8 9.4c.9 2.3 3.3 4.7 5.6 5.6l1.5-1.4c.5-.5 1.2-.5 1.7 0l2.7 2.7c.5.5.5 1.2 0 1.7l-1.6 1.6c-.8.8-2 1-3 .6C9.7 18.3 5.7 14.3 3.8 9.1c-.4-1-.2-2.2.6-3l1.6-1.6c.1-.5.1-.5.6-1z"/><path fill="none" stroke="#33461f" stroke-width="1.6" stroke-linecap="round" d="M13.5 3.5a7 7 0 0 1 7 7M13.5 7a3.5 3.5 0 0 1 3.5 3.5"/></svg>
      0462305178
    </li>
    <li>
      <svg viewBox="0 0 24 24" aria-hidden="true"><rect x="1" y="5" width="22" height="14" fill="#33461f"/><path fill="none" stroke="#fff" stroke-width="1.4" d="M2 6l10 8 10-8M2 18l7.5-6.5M22 18l-7.5-6.5"/></svg>
      carlapenhallow57@mailbox.example
    </li>
    <li>
      <svg viewBox="0 0 24 24" aria-hidden="true"><g fill="none" stroke="#33461f" stroke-width="1.6"><circle cx="12" cy="12" r="10"/><ellipse cx="12" cy="12" rx="4.5" ry="10"/><path d="M2 12h20M3.5 7h17M3.5 17h17M12 2v20"/></g></svg>
      www.thewellnessbarn.example.au
    </li>
  </ul>

  <address class="address">
    <span>4/37 Upper Creekbank Rd</span>
    <span>Tallowbrook</span>
    <span>QLD 4712</span>
  </address>
</section>

</body>
</html>
```